Business card

We need a business card design for our company based in Auckland , New Zealand called 'Quill + Habitat Ltd'. We provide architectural services. We would like to see designs that use the max. three colours (such as white, black, grey) The final design should communicate financial safety and growth."
Also I will provide our company logo. I would like to the logo to be embeded onto our business card.

Target Market(s)

new residential house, alteration & addition & light commericila design & drafting service

Industry/Entity Type

Architecture

Contact Information for Business Card

Company name: quill + habitat Ltd.
Name: Rowan Teale
Job title: architectural designer & Design QWR
email address: rowan@qandh.co.nz
mobile number: 02 5136 2297
web site: www.qandh.co.nz

Requirements
Must have
• My project must have..
• - embeded logo (attached company logo)
• I don't have a bigger version for our company logo, but I have one old one, so you can remove the word from it)
• - insert the attached small GVTK logo & QWR logo
• - creative, simple and clear business card.
• - Max. three colours
Nice to have
• - Here are the samples I would like to share with you: http://www.velmoriq.com/blog/sparse-stationery-layouts/
• I would like to have my business card like one of the creation.
Should not have
• TBA

```html
<!DOCTYPE html>
<html lang="en">
<head>
<meta charset="utf-8">
<title>Quill + Habitat Ltd — Business Card</title>
<link rel="stylesheet" href="https://fonts.googleapis.com/css2?family=Libre+Franklin:wght@400;600;700&display=swap">
<style>
  :root {
    --stage: #3a3b3d;
    --card-white: #ffffff;
    --card-black: #0b0b0b;
    --ink: #111111;
    --grey: #7d8683;
    --grey-light: #b9bcbb;
    --rule: #1a1a1a;
  }
  * { box-sizing: border-box; margin: 0; padding: 0; }
  html, body {
    width: 1200px; height: 950px; overflow: hidden;
    background: var(--stage);
    font-family: "Libre Franklin", Arial, sans-serif;
  }
  .stage {
    position: relative; width: 1200px; height: 950px;
    display: flex; flex-direction: column; align-items: center; justify-content: center; gap: 60px;
  }
  .card {
    position: relative; width: 640px; height: 366px;
    box-shadow: 0 10px 30px rgba(0,0,0,.35);
  }

  /* Back of card */
  .card--back { background: var(--card-black); }
  .back-marks {
    position: absolute; left: 150px; top: 88px;
    display: flex; align-items: center; gap: 30px;
  }
  .member-mark { width: 150px; height: 74px; background: var(--card-white); border-radius: 4px; }
  .marks-divider { width: 1.5px; height: 120px; background: var(--grey-light); }
  .licence-badge { width: 120px; height: 120px; border-radius: 50%; background: var(--grey-light); }
  .back-web {
    position: absolute; left: 0; right: 0; top: 270px; text-align: center;
    color: var(--grey-light); font-size: 17px; letter-spacing: .04em;
  }

  /* Front of card */
  .card--front { background: var(--card-white); }
  .brand {
    position: absolute; right: 40px; top: 122px;
    display: flex; align-items: center; gap: 12px;
  }
  .brand-name { font-size: 18px; font-weight: 600; color: var(--ink); letter-spacing: .02em; }
  .brand-square { width: 14px; height: 14px; background: var(--ink); }
  .identity {
    position: absolute; left: 40px; right: 40px; top: 214px;
    font-size: 21px; font-weight: 700; letter-spacing: .01em;
    padding-bottom: 8px; border-bottom: 2px solid var(--rule);
  }
  .identity .name { color: var(--ink); }
  .identity .sep { color: var(--ink); margin: 0 6px; }
  .identity .role { color: var(--grey); }
  .contact {
    position: absolute; left: 40px; right: 40px; top: 262px;
    font-size: 15px; color: var(--grey); letter-spacing: .02em;
    padding-bottom: 34px; border-bottom: 1px solid var(--rule);
  }
</style>
</head>
<body>
<main class="stage">
  <section class="card card--back" aria-label="Business card reverse">
    <div class="back-marks">
      <div class="member-mark" role="img" aria-label="Professional membership badge"></div>
      <div class="marks-divider"></div>
      <div class="licence-badge" role="img" aria-label="Licensed practitioner badge"></div>
    </div>
    <p class="back-web">www.qandh.co.nz</p>
  </section>

  <section class="card card--front" aria-label="Business card front">
    <div class="brand">
      <span class="brand-name">quill + habitat</span>
      <span class="brand-square" aria-hidden="true"></span>
    </div>
    <h1 class="identity">
      <span class="name">Rowan Teale</span><span class="sep">|</span><span class="role">architectural designer &amp; Design QWR</span>
    </h1>
    <p class="contact">Quill + Habitat Ltd. &nbsp;|&nbsp; M : 02 5136 2297 &nbsp;E : rowan@qandh.co.nz</p>
  </section>
</main>
</body>
</html>
```